Flyer Design Project

I need a cool design that describes a new line of services I am selling. The final product should be a 8 1/2 by 11 and maximum two pages.

I am selling consulting services to learn to use web conferencing tools for business development, meeting and training.

Please use the file I have attached as a guide for your work. It is a document called "primer-thriftyhacksguide" and I love its design.

Thanks

                                        Please substitute the new text availble and just uploaded in the FLYER. Please submit the FINAL version fo your design with TExt changes as well as improvements detailed in previous message. 

Target Market(s)

Entrepreneurs and classroom educators who wnats to explore a new way to teach (innovators not scared of technology)

Industry/Entity Type

Business

Requirements
Must have
• I would like to receive a final PDF with the content EDITABLE for minor edits (I have acrobat)
Logo should be included (attached)

PLEASE CHECK OUT ATTACHED DOCUMENT WHOSE DESIGN I LOVE.
IT is called "Primer thrifty-hacks guide". If you could follow that as a template to design mine that would be great!

```html
<!DOCTYPE html>
<html lang="en">
<head>
<meta charset="utf-8">
<title>Online Meeting Skills Services</title>
<link rel="stylesheet" href="https://fonts.googleapis.com/css2?family=Arimo:wght@400;700&display=swap">
<style>
  :root {
    --orange: #f26f21;
    --brown: #7a3a12;
    --peach: #fbd2b4;
    --blue-dark: #1d2a7a;
    --blue-mid: #2f66b8;
    --blue-light: #7fc3e8;
    --ink: #1f1f1f;
    --white: #ffffff;
  }
  * { margin: 0; padding: 0; box-sizing: border-box; }
  html, body { width: 849px; height: 1200px; overflow: hidden; background: var(--white); }
  .flyer {
    position: relative;
    width: 849px;
    height: 1200px;
    overflow: hidden;
    font-family: "Arimo", Arial, sans-serif;
    color: var(--ink);
    background: var(--white);
  }
  .backdrop { position: absolute; inset: 0; }
  .brand {
    position: absolute;
    left: 40px;
    top: 52px;
    display: flex;
    align-items: center;
    gap: 8px;
    font-weight: 700;
    font-size: 19px;
    letter-spacing: 1.5px;
    color: var(--ink);
  }
  .brand-mark {
    width: 12px; height: 12px;
    border-radius: 50%;
    background: var(--orange);
  }
  .headline {
    position: absolute;
    right: 62px;
    top: 58px;
    text-align: right;
    color: var(--white);
    font-weight: 700;
    line-height: 1;
  }
  .headline-main {
    font-size: 95px;
    letter-spacing: 0.5px;
    line-height: 0.86;
  }
  .headline-sub {
    font-size: 55px;
    margin-top: 14px;
  }
  .headline-tag {
    font-size: 37px;
    margin-top: 6px;
  }
  .question-banner {
    position: absolute;
    left: 228px;
    top: 484px;
    width: 562px;
    height: 82px;
    background: var(--orange);
    border-radius: 22px 0 22px 0;
    color: var(--white);
    font-weight: 700;
    font-size: 20px;
    line-height: 1.45;
    padding: 10px 20px;
  }
  .body-copy {
    position: absolute;
    left: 228px;
    top: 580px;
    width: 584px;
    font-size: 14px;
    line-height: 20px;
    text-align: justify;
  }
  .body-copy p { margin-bottom: 10px; }
  .service-list {
    list-style: none;
    margin: 18px 0 0 20px;
    width: 522px;
  }
  .service-list li {
    position: relative;
    padding-left: 18px;
    margin-bottom: 16px;
    text-align: justify;
  }
  .service-list li::before {
    content: "➥";
    position: absolute;
    left: 0;
    top: 0;
    color: var(--brown);
    font-size: 13px;
  }
</style>
</head>
<body>
<main class="flyer">
  <svg class="backdrop" width="849" height="1200" viewBox="0 0 849 1200">
    <defs>
      <linearGradient id="digitalTone" x1="0" y1="1" x2="1" y2="0">
        <stop offset="0" stop-color="var(--blue-light)"/>
        <stop offset="0.45" stop-color="var(--blue-mid)"/>
        <stop offset="1" stop-color="var(--blue-dark)"/>
      </linearGradient>
      <linearGradient id="peachWash" x1="0" y1="0" x2="0" y2="1">
        <stop offset="0" stop-color="#ffffff"/>
        <stop offset="0.3" stop-color="var(--peach)"/>
        <stop offset="0.7" stop-color="#fff3ea"/>
        <stop offset="1" stop-color="#ffffff"/>
      </linearGradient>
    </defs>
    <rect class="hero-image" x="90" y="0" width="759" height="620" fill="url(#digitalTone)" role="img" aria-label="Blue digital background of binary code and data waves"/>
    <path class="hero-curve" d="M0 590 C 300 500 640 430 849 412 L 849 1200 L 0 1200 Z" fill="var(--white)"/>
    <path class="side-wash" d="M0 0 L 398 0 C 200 200 60 560 10 1200 L 0 1200 Z" fill="url(#peachWash)"/>
    <path class="swoosh" d="M385 0 L 432 0 C 240 170 90 480 30 1200 L 0 1200 L 0 1130 C 30 640 170 230 385 0 Z" fill="var(--orange)"/>
    <path class="swoosh-edge" d="M300 100 C 150 300 62 560 30 900" fill="none" stroke="var(--brown)" stroke-width="4" stroke-linecap="round"/>
  </svg>

  <header class="brand"><span class="brand-mark"></span>CONVENE CONSULTING</header>

  <h1 class="headline">
    <div class="headline-main">ONLINE<br>MEETING</div>
    <div class="headline-sub">SKILLS SERVICES</div>
    <div class="headline-tag">It is just the beginning…</div>
  </h1>

  <h2 class="question-banner">What if your business can reach all the people<br>already interested in learning what you know?</h2>

  <section class="body-copy">
    <p>A different use of webinar technology: the first step towards a new way of thinking about your markets/your clients.</p>
    <p>You probably know about webinars. You may have attended a few yourself. Perhaps you found them boring and un-engaging, with no chance to interact or ask questions to a guarded speaker. Did the speaker drone on as you – yes, you! – checked your email? Good news: we are not talking about “that” kind of webinars. Yes: there is another way!</p>
    <p>Turn your expertise into engaging and interactive online sessions delivered “live”! Engage people online in conversations that matter to them and forget about the technical details, the mailing list or selecting the right webinar technology. We can provide a turnkey solution, that in two-week time offers you all you need to break into this new technology from the front-door. In fact:</p>
    <ul class="service-list">
      <li>We design an effective virtual meeting experience for you using the tools of the online room to their full potential through a different way of thinking about online participant engagement and interactivity.</li>
      <li>We repurpose your marketing materials for engaging collaborative online meeting and learning.</li>
      <li>We develop and execute a communication plan to market your online sessions to your mailing list - already interested in learning about your expertise – and to others.</li>
      <li>We support you “hands-on” as you deliver a synchronous (live and online) session in your own virtual training room. We orchestrate a rehearsal and you show up on the day of the session ready to engage your remote participants.</li>
    </ul>
  </section>
</main>
</body>
</html>
```